Kitchen designer requires a website to showcase work

I require a simple website that will showcase designs, publications, and awards, about and contact. I have attached a couple of ideas that I have found (all kind of different) but we want to pitch this to the high end market, have a nice clean site with amazing images. The Website will be "Marcus Holloway Kitchen Design"

Industry/Entity Type

Kitchen

Coding

Coded - Design and coding required

Number of Pages Required

4 page

Requirements
Must have
• A content management system that I can manage myself

```html
<!DOCTYPE html>
<html lang="en">
<head>
<meta charset="utf-8">
<title>Marcus Holloway Kitchen Designs</title>
<link href="https://fonts.googleapis.com/css2?family=Raleway:wght@300;400;500&family=Open+Sans:wght@400;700&display=swap" rel="stylesheet">
<style>
  :root {
    --brand: #535bc3;
    --ink: #111111;
    --body: #555555;
    --white: #ffffff;
    --photo-light: #e9e8e4;
    --photo-mid: #bdbab3;
    --photo-dark: #6f6c67;
  }
  * { margin: 0; padding: 0; box-sizing: border-box; }
  html, body { width: 1016px; height: 1200px; overflow: hidden; background: var(--white); }
  body { position: relative; font-family: "Raleway", sans-serif; }

  .hero {
    position: absolute; left: 0; top: 0; width: 1016px; height: 661px;
    background:
      linear-gradient(180deg, rgba(0,0,0,0.18) 0%, rgba(0,0,0,0) 20%),
      linear-gradient(100deg, var(--photo-light) 0%, var(--photo-mid) 45%, #d8d6d1 65%, var(--photo-dark) 100%);
  }
  .brand-box {
    position: absolute; left: 65px; top: 0; width: 265px; height: 79px;
    background: var(--white); display: flex; flex-direction: column; justify-content: center;
    padding-left: 18px; color: var(--brand); font-weight: 500; font-size: 17px; line-height: 21px;
    text-transform: uppercase; letter-spacing: 0.2px;
  }
  .brand-box span:last-child { padding-left: 34px; }
  .main-nav {
    position: absolute; top: 38px; left: 375px; display: flex; gap: 22px;
    font-size: 18px; font-weight: 400; color: var(--white);
  }
  .slide-dots { position: absolute; top: 604px; left: 446px; display: flex; gap: 18px; }
  .slide-dots span { width: 17px; height: 17px; background: var(--white); }
  .slide-dots span.is-active { background: var(--brand); }

  .welcome {
    position: absolute; top: 712px; left: 0; width: 1016px;
    display: flex; justify-content: center; align-items: flex-start; gap: 30px;
  }
  .welcome-icon { flex: none; margin-top: 2px; }
  .welcome-title {
    font-weight: 300; font-size: 36px; line-height: 44px; color: var(--ink); text-align: center;
    white-space: nowrap;
  }
  .welcome-title em { font-style: normal; color: var(--brand); }
  .welcome-text {
    position: absolute; top: 823px; left: 0; width: 1016px; text-align: center;
    font-family: "Open Sans", sans-serif; font-size: 12.5px; line-height: 22px; color: var(--body);
  }

  .site-footer {
    position: absolute; left: 4px; top: 989px; width: 1012px; height: 211px; background: var(--brand);
    color: var(--white);
  }
  .footer-nav {
    position: absolute; left: 61px; top: 25px; display: flex; align-items: center; gap: 29px;
    font-size: 15.5px;
  }
  .footer-nav .is-current {
    border: 1px solid var(--white); border-radius: 20px; padding: 9px 20px; margin-right: -9px;
  }
  .footer-call {
    position: absolute; left: 772px; top: 25px; display: flex; align-items: center; gap: 10px;
    font-family: "Open Sans", sans-serif; font-size: 12px;
  }
  .social { position: absolute; left: 424px; top: 99px; display: flex; gap: 18px; }
  .social svg { display: block; }
  .footer-rule { position: absolute; left: 61px; top: 169px; width: 886px; border-top: 1px solid rgba(255,255,255,0.45); }
  .copyright {
    position: absolute; top: 182px; left: 0; width: 1012px; text-align: center;
    font-family: "Open Sans", sans-serif; font-size: 12px;
  }
</style>
</head>
<body>
  <header class="hero" role="img" aria-label="Photograph of a bright modern white kitchen with tall cabinets, island and lounge chair">
    <div class="brand-box"><span>Marcus Holloway</span><span>Kitchen Designs</span></div>
    <nav class="main-nav">
      <span>Home</span><span>Company Profile</span><span>Kitchen</span><span>Cupboards</span><span>Vanities</span><span>Contact</span>
    </nav>
    <div class="slide-dots"><span class="is-active"></span><span></span><span></span><span></span></div>
  </header>

  <section class="welcome">
    <svg class="welcome-icon" width="44" height="44" viewBox="0 0 44 44" aria-hidden="true">
      <circle cx="22" cy="22" r="21" fill="none" stroke="#111" stroke-width="1.2"/>
      <path d="M13 22 L22 14 L31 22 L28.5 22 L28.5 30 L24.5 30 L24.5 25 L19.5 25 L19.5 30 L15.5 30 L15.5 22 Z" fill="#535bc3"/>
    </svg>
    <h1 class="welcome-title">WELCOME TO <em>MARCUS HOLLOWAY</em><br>KITCHEN DESIGNS</h1>
  </section>
  <p class="welcome-text">
    Marcus Holloway Kitchen Designs cc has been serving the Gauteng community for over 20 years.<br>
    We specialize in the design, manufacture and installation of beautiful kitchens, cupboards and vanities.<br>
    Our friendly and professional staff is here to answer any questions you may have about our company or our services.<br>
    Whether you need a completely new installation of your dream kitchen or a new vanity in your bathroom, we have what you need.<br>
    At Marcus Holloway Kitchen Designs cc, our goal is to provide you with courteous, expedient, professional service of the highest caliber.
  </p>

  <footer class="site-footer">
    <nav class="footer-nav">
      <span class="is-current">Home</span><span>Company Profile</span><span>Kitchen</span><span>Cupboards</span><span>Vanities</span><span>Contact</span>
    </nav>
    <div class="footer-call">
      <svg width="36" height="36" viewBox="0 0 36 36" aria-hidden="true">
        <circle cx="18" cy="18" r="18" fill="#fff"/>
        <rect x="13" y="10" width="10" height="16" rx="2" fill="none" stroke="#535bc3" stroke-width="2"/>
        <circle cx="18" cy="23" r="1" fill="#535bc3"/>
      </svg>
      <span>Call : 010 555 0142</span>
    </div>
    <div class="social" aria-label="Social links">
      <svg width="44" height="44" viewBox="0 0 44 44" aria-label="Email">
        <circle cx="22" cy="22" r="21.5" fill="none" stroke="#fff" stroke-width="1"/>
        <g fill="none" stroke="rgba(255,255,255,0.55)" stroke-width="1.8">
          <rect x="14" y="16" width="16" height="12" rx="1"/>
          <path d="M14 17 L22 23 L30 17"/>
        </g>
      </svg>
      <svg width="44" height="44" viewBox="0 0 44 44" aria-label="Share">
        <circle cx="22" cy="22" r="21.5" fill="none" stroke="#fff" stroke-width="1"/>
        <g fill="#fff"><circle cx="16" cy="22" r="3"/><circle cx="28" cy="15" r="3"/><circle cx="28" cy="29" r="3"/></g>
        <path d="M16 22 L28 15 M16 22 L28 29" stroke="#fff" stroke-width="1.8"/>
      </svg>
      <svg width="44" height="44" viewBox="0 0 44 44" aria-label="Website">
        <circle cx="22" cy="22" r="21.5" fill="none" stroke="#fff" stroke-width="1"/>
        <g fill="none" stroke="#fff" stroke-width="1.8">
          <circle cx="22" cy="22" r="9"/>
          <ellipse cx="22" cy="22" rx="4" ry="9"/>
          <path d="M13 22 H31"/>
        </g>
      </svg>
    </div>
    <div class="footer-rule"></div>
    <p class="copyright">© <strong>MARCUS HOLLOWAY KITCHEN DESIGNS</strong> - 2015. All Rights Reserved.</p>
  </footer>
</body>
</html>
```